Business Card Design Project

We are an agricultural business based in Brisbane.
We design, manage and operate regional saleyards. Our logo is green/silver in colour and details of our business can be found on our website www.tovrak.com.au

Just wanting a corporate design for some business cards and include name, position, contact details.

Thanks

```html
<!DOCTYPE html>
<html lang="en">
<head>
<meta charset="utf-8">
<title>Tovrak Saleyards – Business Card</title>
<link rel="stylesheet" href="https://fonts.googleapis.com/css2?family=Open+Sans:wght@400;600;700&display=swap">
<style>
  :root {
    --backdrop: #ebe8e5;
    --card: #ffffff;
    --ink: #111111;
    --ink-soft: #3a3a3a;
    --rule: #8c8c8c;
    --silver: #8f9091;
    --green: #137a37;
  }
  * { box-sizing: border-box; margin: 0; padding: 0; }
  html, body {
    width: 1200px; height: 960px; overflow: hidden;
    background: var(--backdrop);
    font-family: "Open Sans", Arial, sans-serif;
  }
  .canvas {
    width: 1200px; height: 960px;
    display: flex; flex-direction: column;
    align-items: center; justify-content: center; gap: 60px;
  }
  .card {
    position: relative;
    width: 680px; height: 388px;
    background: var(--card);
    box-shadow: 0 6px 18px rgba(0,0,0,0.12);
    overflow: hidden;
  }
  /* Contact side */
  .card-contact .corner-shapes { position: absolute; inset: 0; }
  .card-contact .brand-name {
    position: absolute; left: 40px; top: 88px;
    font-size: 30px; font-weight: 700; letter-spacing: 2px;
    color: var(--ink);
  }
  .details {
    position: absolute; left: 350px; top: 58px; width: 290px;
    color: var(--ink-soft);
  }
  .person-name {
    font-size: 27px; font-weight: 700; color: var(--ink);
    padding-bottom: 6px; border-bottom: 1px solid var(--rule);
  }
  .person-role {
    font-size: 12px; padding: 6px 0 10px 14px; position: relative;
    border-bottom: 1px solid var(--rule);
  }
  .contact-list { list-style: none; margin-top: 14px; }
  .contact-list li {
    font-size: 11.5px; line-height: 1.55; padding-left: 14px; position: relative;
  }
  .contact-list li.group-start { margin-top: 10px; }
  .contact-list li.group-start:first-child { margin-top: 0; }
  .marker::before, .person-role::before {
    content: ""; position: absolute; left: 0; top: 7px;
    border-left: 4px solid transparent; border-right: 4px solid transparent;
    border-top: 5px solid var(--ink);
  }
  .person-role::before { top: 11px; }
  /* Brand side */
  .card-brand {
    display: flex; flex-direction: column; align-items: center; justify-content: center;
  }
  .card-brand .brand-name {
    font-size: 64px; font-weight: 700; letter-spacing: 4px; line-height: 1.05;
    color: var(--ink); text-align: center;
  }
</style>
</head>
<body>
<main class="canvas">
  <section class="card card-contact" aria-label="Business card, contact side">
    <svg class="corner-shapes" viewBox="0 0 680 388" width="680" height="388" aria-hidden="true">
      <polygon points="0,0 320,0 292,110 0,110" fill="var(--silver)"/>
      <polygon points="0,110 292,110 170,388 150,388" fill="var(--green)"/>
    </svg>
    <div class="brand-name">TOVRAK</div>
    <div class="details">
      <h1 class="person-name">Daniel Whitford</h1>
      <p class="person-role">Chief Executive Officer - TOVRAK</p>
      <ul class="contact-list">
        <li class="group-start marker">Australia</li>
        <li>2207 Harbour Field Rd, Suite 12</li>
        <li>Brisbane, QLD 4000</li>
        <li class="group-start marker">Email: daniel@tovrak.com.au</li>
        <li>Mob: 0491 570 318</li>
        <li>www.tovrak.com.au</li>
      </ul>
    </div>
  </section>
  <section class="card card-brand" aria-label="Business card, brand side">
    <div class="brand-name">TOVRAK<br>SALEYARDS</div>
  </section>
</main>
</body>
</html>
```